Banner Ad Design Project: rovalenmotors.com

Google all ad dimensions banner pack for http://www.rovalenmotors.com.

Ad dimensions Max. file sizes (KB) Ad types
468 × 60 50 Banner
728 × 90 50 Leaderboard
250 × 250 50 Square
200 × 200 50 Small square
336 × 280 50 Large rectangle
300 × 250 50 Inline rectangle
120 × 600 50 Skyscraper
160 × 600 50 Wide skyscraper
300 × 600 200 Half-page ad
970 × 90 200 Large leaderboard
240 × 400 50 Vertical rectangle
980 × 120 200 Panorama
930 × 180 200 Top banner
250 × 360 50 Triple widescreen
580 × 400 200 Netboard

*Please visit the website and come up with unique ideas.

Target Market(s)

Consumers looking to transport a car, motor vehicle, motorcycle or anything that has wheels and a motor in the united states long distance.

Industry/Entity Type

Google

Requirements
Must have
• a call to action for example (RANDOM ONE):
-
TALK TO A REAL CAR SHIPPING PRO NOW: 1-888-514-2763
HAVE CAR TRANSPORT QUESTIONS? CALL NOW: 1-888-514-2763
CALL NOW & TALK TO A REAL AUTO SHIPPING EXPERT: 1-888-514-2763
Call Now Free Quote:1-888-514-2763

Nice to have
• Best Value For Dollar Auto Transport
Bonded, Insured & Licensed
Price Match Guarantee: will match any price by a 4 or 5 star rated Company.
Best of all, you pay nothing until your car is picked up!
Nationwide Door-To-Door Vehicle Shipping
Should not have
• Logo integrated in to the design.
bold call to action; ex; call now free quote:
Heading style phone number, 888-514-2763, stands out and screams call now.
example:
CALL ROVALEN TODAY TO TRANSPORT YOUR VEHICLE
1-888-514-2763

```html
<!DOCTYPE html>
<html lang="en">
<head>
<meta charset="utf-8">
<title>Rovalen Motors – Car Transport Banner Pack</title>
<link rel="stylesheet" href="https://fonts.googleapis.com/css2?family=Roboto+Condensed:wght@700&display=swap">
<style>
  :root {
    --stage: #ebe7e2;
    --navy-deep: #1c2536;
    --navy-mid: #2f4361;
    --navy-light: #56779f;
    --stripe: #5c86b8;
    --band: #ffffff;
    --silver-top: #ffffff;
    --silver-bottom: #c9ced6;
    --gold-top: #ffd11f;
    --gold-bottom: #f39a0b;
    --brand-blue: #3d82c4;
    --photo-skin: #e6c3a0;
    --photo-hair: #d8b467;
    --photo-shirt: #f1f2f5;
  }
  * { margin: 0; padding: 0; box-sizing: border-box; }
  html, body { width: 1200px; height: 760px; overflow: hidden; }
  body {
    background: var(--stage);
    font-family: "Roboto Condensed", "Arial Narrow", sans-serif;
    font-weight: 700;
    position: relative;
  }

  /* ---- shared banner parts ---- */
  .ad {
    position: absolute;
    overflow: hidden;
    background: linear-gradient(180deg, var(--navy-deep) 0%, var(--navy-mid) 45%, var(--navy-light) 100%);
    box-shadow: 0 4px 14px rgba(0,0,0,.25);
  }
  .ad > * { position: absolute; }
  .ask, .cta {
    line-height: 1;
    white-space: nowrap;
    text-transform: uppercase;
    letter-spacing: -0.02em;
  }
  .silver {
    background: linear-gradient(180deg, var(--silver-top) 30%, var(--silver-bottom) 100%);
    -webkit-background-clip: text;
    background-clip: text;
    color: transparent;
    filter: drop-shadow(0 2px 1px rgba(0,0,0,.55));
  }
  .gold {
    background: linear-gradient(180deg, var(--gold-top) 20%, var(--gold-bottom) 100%);
    -webkit-background-clip: text;
    background-clip: text;
    color: transparent;
    filter: drop-shadow(0 2px 1px rgba(0,0,0,.55));
  }
  .photo {
    background:
      radial-gradient(ellipse 38% 30% at 55% 38%, var(--photo-skin) 0%, rgba(230,195,160,0) 100%),
      radial-gradient(ellipse 55% 42% at 50% 30%, var(--photo-hair) 0%, rgba(216,180,103,0) 100%),
      linear-gradient(180deg, #e9e3da 0%, var(--photo-shirt) 70%);
  }
  .band {
    background: var(--band);
    border-top: 4px solid var(--stripe);
  }
  .band::before {
    content: "";
    position: absolute;
    top: -11px;
    left: 36px;
    border: 7px solid transparent;
    border-bottom-color: var(--band);
  }
  .brand {
    display: flex;
    align-items: center;
    gap: 7px;
    color: var(--brand-blue);
    line-height: 1;
  }
  .brand__mark {
    width: .8em;
    height: .8em;
    background: var(--brand-blue);
  }

  /* ---- netboard ---- */
  .ad--netboard { left: 258px; top: 135px; width: 546px; height: 376px; }
  .ad--netboard .ask--lead { left: 0; right: 0; top: 16px; text-align: center; font-size: 38px; }
  .ad--netboard .ask--main { left: 0; right: 0; top: 52px; text-align: center; font-size: 76px; }
  .ad--netboard .cta--label { left: 84px; top: 168px; font-size: 46px; }
  .ad--netboard .cta--phone { left: 56px; top: 222px; font-size: 37px; }
  .ad--netboard .band { left: 0; top: 276px; width: 330px; height: 100px; }
  .ad--netboard .band::before { left: 34px; }
  .ad--netboard .brand { left: 56px; top: 322px; font-size: 30px; }
  .ad--netboard .photo { left: 330px; top: 130px; width: 216px; height: 246px; }

  /* ---- skyscraper ---- */
  .ad--skyscraper { left: 64px; top: 135px; width: 150px; height: 565px; }
  .ad--skyscraper .ask { left: 0; right: 0; text-align: center; }
  .ad--skyscraper .ask--l1 { top: 20px; font-size: 31px; }
  .ad--skyscraper .ask--l2 { top: 56px; font-size: 27px; }
  .ad--skyscraper .ask--main { top: 88px; font-size: 25px; }
  .ad--skyscraper .cta { left: 0; right: 0; text-align: center; }
  .ad--skyscraper .cta--label { top: 166px; font-size: 25px; }
  .ad--skyscraper .cta--phone { top: 198px; font-size: 20px; }
  .ad--skyscraper .photo { left: 0; top: 268px; width: 150px; height: 192px; }
  .ad--skyscraper .band { left: 0; top: 458px; width: 150px; height: 107px; }
  .ad--skyscraper .band::before { left: 26px; }
  .ad--skyscraper .brand { left: 22px; top: 540px; font-size: 22px; }

  /* ---- square ---- */
  .ad--square { left: 868px; top: 64px; width: 282px; height: 235px; }
  .ad--square .photo { left: 0; top: 0; width: 100px; height: 152px; }
  .ad--square .ask, .ad--square .cta { right: 10px; text-align: right; }
  .ad--square .ask--lead { top: 14px; font-size: 17px; }
  .ad--square .ask--main { top: 33px; font-size: 31px; }
  .ad--square .cta--label { top: 92px; right: 16px; font-size: 22px; }
  .ad--square .cta--phone { top: 118px; right: 12px; font-size: 19px; }
  .ad--square .band { left: 0; top: 152px; width: 282px; height: 83px; }
  .ad--square .band::before { left: 20px; }
  .ad--square .brand { left: 118px; top: 208px; font-size: 24px; }

  /* ---- rectangle ---- */
  .ad--rectangle { left: 852px; top: 323px; width: 316px; height: 263px; }
  .ad--rectangle .photo { left: 0; top: 0; width: 110px; height: 178px; }
  .ad--rectangle .ask, .ad--rectangle .cta { right: 12px; text-align: right; }
  .ad--rectangle .ask--lead { top: 16px; font-size: 19px; }
  .ad--rectangle .ask--main { top: 37px; font-size: 35px; }
  .ad--rectangle .cta--label { top: 106px; right: 28px; font-size: 25px; }
  .ad--rectangle .cta--phone { top: 137px; right: 14px; font-size: 22px; }
  .ad--rectangle .band { left: 0; top: 178px; width: 316px; height: 85px; }
  .ad--rectangle .band::before { left: 20px; }
  .ad--rectangle .brand { left: 142px; top: 236px; font-size: 26px; }

  /* ---- banner ---- */
  .ad--banner { left: 318px; top: 544px; width: 440px; height: 55px; }
  .ad--banner .band { left: 0; top: 0; width: 112px; height: 55px; border-top: 0; border-right: 3px solid var(--stripe); }
  .ad--banner .band::before { display: none; }
  .ad--banner .brand { left: 14px; top: 27px; font-size: 16px; gap: 5px; }
  .ad--banner .ask--lead { left: 124px; top: 8px; font-size: 13px; }
  .ad--banner .ask--main { left: 122px; top: 23px; font-size: 25px; }
  .ad--banner .photo { left: 268px; top: 0; width: 62px; height: 55px; }
  .ad--banner .cta { text-align: right; }
  .ad--banner .cta--label { right: 14px; top: 9px; font-size: 17px; }
  .ad--banner .cta--phone { right: 6px; top: 31px; font-size: 13px; }

  /* ---- leaderboard ---- */
  .ad--leaderboard { left: 258px; top: 623px; width: 685px; height: 84px; }
  .ad--leaderboard .band { left: 0; top: 0; width: 172px; height: 84px; border-top: 0; border-right: 4px solid var(--stripe); }
  .ad--leaderboard .band::before { display: none; }
  .ad--leaderboard .brand { left: 26px; top: 44px; font-size: 24px; }
  .ad--leaderboard .ask--lead { left: 198px; top: 14px; font-size: 20px; }
  .ad--leaderboard .ask--main { left: 194px; top: 36px; font-size: 38px; }
  .ad--leaderboard .photo { left: 400px; top: 0; width: 110px; height: 84px; }
  .ad--leaderboard .cta { text-align: right; }
  .ad--leaderboard .cta--label { right: 36px; top: 16px; font-size: 27px; }
  .ad--leaderboard .cta--phone { right: 14px; top: 48px; font-size: 22px; }
</style>
</head>
<body>

  <section class="ad ad--skyscraper" aria-label="Skyscraper ad">
    <p class="ask ask--l1 silver">Have Car</p>
    <p class="ask ask--l2 silver">Transport</p>
    <p class="ask ask--main gold">Questions?</p>
    <p class="cta cta--label silver">Call Now</p>
    <p class="cta cta--phone gold">1-888-514-2763</p>
    <div class="photo" role="img" aria-label="Photo of a smiling support agent wearing a headset"></div>
    <div class="band"></div>
    <div class="brand"><span class="brand__mark"></span><span class="brand__name">ROVALEN</span></div>
  </section>

  <section class="ad ad--netboard" aria-label="Netboard ad">
    <p class="ask ask--lead silver">Have Car Transport</p>
    <p class="ask ask--main gold">Questions?</p>
    <p class="cta cta--label silver">Call Now</p>
    <p class="cta cta--phone gold">1-888-514-2763</p>
    <div class="band"></div>
    <div class="brand"><span class="brand__mark"></span><span class="brand__name">ROVALEN</span></div>
    <div class="photo" role="img" aria-label="Photo of a smiling support agent wearing a headset"></div>
  </section>

  <section class="ad ad--square" aria-label="Square ad">
    <div class="photo" role="img" aria-label="Photo of a smiling support agent wearing a headset"></div>
    <p class="ask ask--lead silver">Have Car Transport</p>
    <p class="ask ask--main gold">Questions?</p>
    <p class="cta cta--label silver">Call Now</p>
    <p class="cta cta--phone gold">1-888-514-2763</p>
    <div class="band"></div>
    <div class="brand"><span class="brand__mark"></span><span class="brand__name">ROVALEN</span></div>
  </section>

  <section class="ad ad--rectangle" aria-label="Rectangle ad">
    <div class="photo" role="img" aria-label="Photo of a smiling support agent wearing a headset"></div>
    <p class="ask ask--lead silver">Have Car Transport</p>
    <p class="ask ask--main gold">Questions?</p>
    <p class="cta cta--label silver">Call Now</p>
    <p class="cta cta--phone gold">1-888-514-2763</p>
    <div class="band"></div>
    <div class="brand"><span class="brand__mark"></span><span class="brand__name">ROVALEN</span></div>
  </section>

  <section class="ad ad--banner" aria-label="Banner ad">
    <div class="band"></div>
    <div class="brand"><span class="brand__mark"></span><span class="brand__name">ROVALEN</span></div>
    <p class="ask ask--lead silver">Have Car Transport</p>
    <p class="ask ask--main gold">Questions?</p>
    <div class="photo" role="img" aria-label="Photo of a smiling support agent wearing a headset"></div>
    <p class="cta cta--label silver">Call Now</p>
    <p class="cta cta--phone gold">1-888-514-2763</p>
  </section>

  <section class="ad ad--leaderboard" aria-label="Leaderboard ad">
    <div class="band"></div>
    <div class="brand"><span class="brand__mark"></span><span class="brand__name">ROVALEN</span></div>
    <p class="ask ask--lead silver">Have Car Transport</p>
    <p class="ask ask--main gold">Questions?</p>
    <div class="photo" role="img" aria-label="Photo of a smiling support agent wearing a headset"></div>
    <p class="cta cta--label silver">Call Now</p>
    <p class="cta cta--phone gold">1-888-514-2763</p>
  </section>

</body>
</html>
```